ecommerce news podcast artwork

Podcast cover art for a podcast featuring daily news and events around ecommerce product businesses.

text to be: TILLWIRE
optional third line of text with smaller font: Podcast

looking for something that pops with a medium to light blue background. text can be in white/red/orange colors. prefer solid colors for text, but background can vary.
I'm really open to other ideas too, sometimes you don't know what you want until you see it.

Target Market(s)

ecommerce business owners, managers

Industry/Entity Type

news, business, ecommerce

Font styles to use
Sans Serif

Colors
0054AA
0677BA
7BADD7
CADEEF
E8F1F8
0094D4
00A9DD
6FCCEA
C7EBF8
E9F6FB
F0912C
F2A743
F7CA91
FBE8D2
FDF5EE
EB3D1F
EC4F4E
F09395
F8D3D4
FCEDEE

Requirements
Must have
• text: TILLWIRE
Should not have
• no microphones, headsets/headphones, speakers, or other props like that.

```html
<!DOCTYPE html>
<html lang="en">
<head>
<meta charset="utf-8">
<title>TILLWIRE Podcast Cover</title>
<link rel="stylesheet" href="https://fonts.googleapis.com/css2?family=Archivo+Black&family=Montserrat:wght@500&display=swap">
<style>
  :root {
    --ink: #0d0b14;
    --red: #ff0000;
    --signal-red: #eb3d1f;
    --orange: #f0912c;
    --white: #ffffff;
    --sky-edge: #3fc4f7;
    --sky-mid: #aee6fb;
    --sky-center: #ffffff;
    --art-a: #f2a743;
    --art-b: #00a9dd;
    --art-c: #ec4f4e;
    --art-d: #9b59a6;
    --cart-red: #b3201f;
    --cart-grey: #a9a9a9;
    --bag-green: #23a38a;
  }
  html, body {
    margin: 0;
    padding: 0;
    width: 1200px;
    height: 1200px;
    overflow: hidden;
  }
  .cover {
    position: relative;
    width: 1200px;
    height: 1200px;
    background: radial-gradient(circle at 50% 52%, var(--sky-center) 0%, var(--sky-center) 38%, var(--sky-mid) 72%, var(--sky-edge) 100%);
    overflow: hidden;
  }
  .cover-graphics {
    position: absolute;
    inset: 0;
    width: 1200px;
    height: 1200px;
  }
  .title-main {
    font-family: "Archivo Black", sans-serif;
    fill: var(--ink);
  }
  .title-badge-text {
    font-family: "Archivo Black", sans-serif;
    fill: var(--white);
    stroke: var(--orange);
    stroke-width: 4;
    paint-order: stroke;
  }
  .subtitle {
    font-family: "Montserrat", sans-serif;
    font-weight: 500;
    fill: var(--ink);
    letter-spacing: 6px;
  }
  .icon-bubbles {
    position: absolute;
    left: 152px;
    top: 530px;
    width: 246px;
    height: 256px;
    border-radius: 50%;
    background: radial-gradient(circle at 45% 40%, var(--art-d) 0%, var(--art-c) 40%, var(--art-a) 65%, var(--art-b) 90%);
  }
  .shopping-cart {
    position: absolute;
    left: 330px;
    top: 760px;
    width: 232px;
    height: 270px;
    border-radius: 40px 40px 24px 24px;
    background: linear-gradient(180deg, var(--bag-green) 0%, var(--cart-red) 35%, var(--cart-red) 70%, var(--cart-grey) 100%);
  }
</style>
</head>
<body>
<main class="cover">
  <div class="icon-bubbles" role="img" aria-label="Cluster of overlapping colourful circles holding small ecommerce icons"></div>
  <div class="shopping-cart" role="img" aria-label="Illustration of a red shopping cart filled with gift bags and parcels"></div>

  <svg class="cover-graphics" viewBox="0 0 1200 1200" xmlns="http://www.w3.org/2000/svg">
    <text class="title-main" x="146" y="493" font-size="395" textLength="916" lengthAdjust="spacingAndGlyphs">TILL</text>

    <g class="badge-accents">
      <polygon points="408,548 470,584 466,592 404,558" fill="var(--red)"/>
      <polygon points="412,680 468,640 470,648 418,690" fill="var(--ink)"/>
      <polygon points="1062,542 1002,580 1008,586 1070,552" fill="var(--ink)"/>
      <polygon points="1002,664 1062,712 1054,720 1000,672" fill="var(--red)"/>
    </g>

    <rect class="title-badge" x="481" y="526" width="510" height="202" rx="16" fill="var(--red)"/>
    <text class="title-badge-text" x="736" y="702" font-size="172" text-anchor="middle" textLength="448" lengthAdjust="spacingAndGlyphs">WIRE</text>

    <g class="signal-left" fill="none" stroke="var(--signal-red)" stroke-width="5" stroke-linecap="round">
      <circle cx="577" cy="773" r="3" fill="var(--signal-red)" stroke="none"/>
      <path d="M570 762 a14 14 0 0 0 0 22"/>
      <path d="M562 754 a24 24 0 0 0 0 38"/>
    </g>
    <text class="subtitle" x="740" y="793" font-size="49" text-anchor="middle" textLength="290">PODCAST</text>
    <g class="signal-right" fill="none" stroke="var(--signal-red)" stroke-width="5" stroke-linecap="round">
      <circle cx="903" cy="773" r="3" fill="var(--signal-red)" stroke="none"/>
      <path d="M910 762 a14 14 0 0 1 0 22"/>
      <path d="M918 754 a24 24 0 0 1 0 38"/>
    </g>
  </svg>
</main>
</body>
</html>
```